Email Signature

We are looking for creative email signature for our company. Please find attached the logo of our company for your reference. now we understand there isn't much can be done with email signature but we are looking for out of the box designs. Nothing specific in mind

Please insert fake numbers, website and/or address, etc just to showcase the designs. once the design is chosen we will provide the actual details.
Updates

Dear All,

We wouldlike to extend our apology for not being able to provide feedbacks to everysingle design. We were extremely busy and we have multiple contests opensimultaneously which makes the process harder. However, thank you all for theefforts you have put into this contest. We have received anoverwhelming quality responses & it has been a very difficult task tochoose just one, we easily Loved at least several designs...

Thanksagain for participating, we wish you all success in your design ventures.

Kindregards,

HLW Team

Industry/Entity Type

It Company

```html
<!DOCTYPE html>
<html lang="en">
<head>
<meta charset="utf-8">
<title>Harbor Lantern – Email Signature</title>
<link rel="stylesheet" href="https://fonts.googleapis.com/css2?family=Varela+Round&display=swap">
<style>
  :root {
    --paper: #ffffff;
    --brand-blue: #1e7fd6;
    --text-blue: #2b72bd;
    --rule-blue: #3a8fd8;
    --brand-green: #7dc21e;
  }
  html, body {
    margin: 0;
    padding: 0;
    overflow: hidden;
    background: var(--paper);
  }
  .signature {
    position: relative;
    width: 1200px;
    height: 662px;
    background: var(--paper);
    font-family: "Varela Round", sans-serif;
    overflow: hidden;
  }
  .brand {
    position: absolute;
    left: 205px;
    top: 250px;
    width: 290px;
    height: 150px;
  }
  .brand-dot {
    position: absolute;
    left: 0;
    top: 15px;
    width: 120px;
    height: 120px;
    border-radius: 50%;
    background: var(--brand-green);
  }
  .brand-name {
    position: absolute;
    left: 134px;
    top: 48px;
    margin: 0;
    font-size: 24px;
    line-height: 1.15;
    font-weight: 400;
    color: var(--brand-blue);
  }
  .brand-phone {
    position: absolute;
    left: 134px;
    top: 108px;
    margin: 0;
    font-size: 15px;
    color: var(--brand-blue);
    white-space: nowrap;
  }
  .contact {
    position: absolute;
    left: 505px;
    top: 294px;
    width: 470px;
  }
  .contact-web {
    margin: 0;
    font-size: 21px;
    line-height: 28px;
    color: var(--brand-blue);
    white-space: nowrap;
    word-spacing: 2px;
  }
  .contact-web .gap { display: inline-block; width: 18px; }
  .contact-rule {
    height: 2px;
    margin: 3px 0 4px -3px;
    width: 473px;
    background: var(--rule-blue);
  }
  .contact-address {
    margin: 0;
    font-size: 20px;
    line-height: 28px;
    color: var(--text-blue);
    white-space: nowrap;
  }
</style>
</head>
<body>
  <main class="signature">
    <div class="brand">
      <div class="brand-dot"></div>
      <p class="brand-name">Harbor<br>Lantern</p>
      <p class="brand-phone">ph. 555-019274</p>
    </div>
    <div class="contact">
      <p class="contact-web">www.hlworks.com<span class="gap"></span>email:info@hlworks.com</p>
      <div class="contact-rule"></div>
      <p class="contact-address">14 Quay Lane,Harbour Point 2011,NSW Australia</p>
    </div>
  </main>
</body>
</html>
```